Brightfork Brine Co, we sell different color pickles that are different flavors

I need nice packaging done for my product, I sell different color pickles.
1. Uploaded photo of my logo, packaging inspiration, also the nutrition facts I want on the packaging as well.
2. This is the stuff I want on my packaging. Packaging, Refrigerator after opening
Packaging, Fresh packaging
Packaging, liquid inside, be careful while opening
Packaging, resealable
Packaging, social media, instragram: @brightforkbrineco and Facebook: @brightforkbrineco
Packaging, sku

Product description:
Looking for a delicious and refreshing snack? Look no further than Brightfork Brine Co! Our pickles are crunchy and full of flavor, and they make a great addition to any meal. We offer a variety of flavors, so there's something for everyone to enjoy. Be sure to check us out today! You won't be disappointed!

Nutrition label on back of packaging, uploaded it

Target Market(s)

Pickle lovers, kids

Font styles to use
Decorative

Colors

Designer to choose colors to be used in the design.

Requirements
Must have
• Bright colors, friendly looking, eye catching
Nice to have
• My social media on my packaging, the flavor, the fruit of the flavor on the package with water on it
Should not have
• Dark colors

```html
<!DOCTYPE html>
<html lang="en">
<head>
<meta charset="utf-8">
<title>Brightfork Brine Co – Crunchy Pickles Pouches</title>
<link href="https://fonts.googleapis.com/css2?family=Bebas+Neue&family=Oswald:wght@300;400;600&display=swap" rel="stylesheet">
<style>
  :root{
    --bg:#ffffff;
    --grape-light:#a45bb8;
    --grape:#7a2a8e;
    --grape-dark:#5e1870;
    --grape-band:#6a1a7e;
    --apple-light:#8fcb5a;
    --apple:#4f9a2f;
    --apple-dark:#3a7d22;
    --apple-band:#137a45;
    --berry-light:#e0474f;
    --berry:#c0222e;
    --berry-dark:#9a1520;
    --berry-band:#8e0d14;
    --teal:#1a9a94;
    --teal-light:#22aea0;
    --white:#ffffff;
    --soft-white:#e9e6ec;
  }
  *{box-sizing:border-box;margin:0;padding:0}
  html,body{width:1200px;height:873px;overflow:hidden;background:var(--bg)}
  .canvas{position:relative;width:1200px;height:873px;background:var(--bg)}

  .pouch{position:absolute;width:398px;height:647px;overflow:hidden;
    font-family:'Oswald',sans-serif;color:var(--white);
    box-shadow:0 6px 18px rgba(0,0,0,.18)}
  .pouch--grape{left:49px;top:94px;
    background:radial-gradient(ellipse at 50% 45%,var(--grape-light) 0%,var(--grape) 55%,var(--grape-dark) 100%)}
  .pouch--apple{left:402px;top:129px;z-index:2;
    background:radial-gradient(ellipse at 50% 45%,var(--apple-light) 0%,var(--apple) 55%,var(--apple-dark) 100%)}
  .pouch--berry{left:755px;top:94px;
    background:radial-gradient(ellipse at 50% 45%,var(--berry-light) 0%,var(--berry) 55%,var(--berry-dark) 100%)}

  .lower-strip{position:absolute;left:0;right:0;top:533px;height:104px;background:rgba(255,255,255,.08)}

  .brand-name{position:absolute;left:60px;width:290px;top:128px;text-align:center;
    font-family:'Bebas Neue',sans-serif;font-size:46px;line-height:44px;color:var(--white);letter-spacing:1px}

  .product-photo{position:absolute;left:71px;top:259px;width:262px;height:164px;border-radius:50%/40%}
  .pouch--grape .product-photo{background:radial-gradient(ellipse at 55% 45%,#b45ad6 0%,#6e2597 55%,rgba(80,20,110,0) 75%)}
  .pouch--apple .product-photo{background:radial-gradient(ellipse at 55% 45%,#c8e56a 0%,#6aa530 55%,rgba(60,120,30,0) 75%)}
  .pouch--berry .product-photo{background:radial-gradient(ellipse at 55% 45%,#f06060 0%,#a81822 55%,rgba(130,15,25,0) 75%)}

  .product-title{position:absolute;left:62px;top:434px;width:280px;
    font-family:'Bebas Neue',sans-serif;font-size:52px;line-height:52px;white-space:nowrap;
    color:var(--soft-white);text-shadow:0 2px 3px rgba(0,0,0,.3)}

  .flavor-band{position:absolute;left:66px;top:486px;width:169px;height:30px;
    transform:skewX(-8deg);display:flex;align-items:center;justify-content:center}
  .flavor-band span{transform:skewX(8deg);font-family:'Bebas Neue',sans-serif;font-size:28px;line-height:30px;color:var(--soft-white)}
  .pouch--grape .flavor-band{background:var(--grape-band)}
  .pouch--apple .flavor-band{background:var(--apple-band)}
  .pouch--berry .flavor-band{background:var(--berry-band)}

  .fresh-note{position:absolute;left:246px;top:488px;font-weight:300;font-size:20px;color:var(--soft-white);
    transform:scaleX(.85);transform-origin:left}

  .care-label{position:absolute;left:69px;top:536px;width:125px;height:79px;border-radius:6px;
    background:linear-gradient(135deg,var(--teal) 0%,var(--teal-light) 100%);transform:rotate(-2deg);
    text-align:center;padding-top:6px;box-shadow:0 2px 4px rgba(0,0,0,.2)}
  .care-label .care-title{font-size:22px;line-height:24px;font-weight:400;transform:scaleX(.8)}
  .care-label .care-line{font-size:8.5px;font-weight:600;line-height:12px}
  .care-label .care-rule{height:3px;background:var(--white);margin:4px 6px 5px;border-radius:2px}

  .social{position:absolute;left:210px;top:538px;width:138px;text-align:center;color:var(--soft-white)}
  .social .follow{font-size:30px;line-height:34px;font-weight:300;transform:scaleX(.82)}
  .social .networks{font-size:11.5px;font-weight:400;line-height:14px}
  .social .handle{font-size:20px;font-weight:300;line-height:26px;transform:scaleX(.8);white-space:nowrap}
</style>
</head>
<body>
<main class="canvas">

  <section class="pouch pouch--grape" aria-label="Grape flavor pouch">
    <div class="lower-strip"></div>
    <div class="brand-name">Brightfork<br>Brine Co</div>
    <div class="product-photo" role="img" aria-label="Photo of purple grape-flavored pickles, one cut open"></div>
    <h2 class="product-title">CRUNCHY PICKLES</h2>
    <div class="flavor-band"><span>GRAPE</span></div>
    <p class="fresh-note">Fresh Packaging</p>
    <div class="care-label">
      <p class="care-title">Liquid Inside</p>
      <p class="care-line">Be careful while opening</p>
      <div class="care-rule"></div>
      <p class="care-line">Refrigerator after opening</p>
    </div>
    <div class="social">
      <p class="follow">Follow Us</p>
      <p class="networks">on our social networks</p>
      <p class="handle">@brightforkbrineco</p>
    </div>
  </section>

  <section class="pouch pouch--apple" aria-label="Green apple flavor pouch">
    <div class="lower-strip"></div>
    <div class="brand-name">Brightfork<br>Brine Co</div>
    <div class="product-photo" role="img" aria-label="Photo of green apple-flavored pickles, one cut open"></div>
    <h2 class="product-title">CRUNCHY PICKLES</h2>
    <div class="flavor-band"><span>GREEN APPLE</span></div>
    <p class="fresh-note">Fresh Packaging</p>
    <div class="care-label">
      <p class="care-title">Liquid Inside</p>
      <p class="care-line">Be careful while opening</p>
      <div class="care-rule"></div>
      <p class="care-line">Refrigerator after opening</p>
    </div>
    <div class="social">
      <p class="follow">Follow Us</p>
      <p class="networks">on our social networks</p>
      <p class="handle">@brightforkbrineco</p>
    </div>
  </section>

  <section class="pouch pouch--berry" aria-label="Strawberry flavor pouch">
    <div class="lower-strip"></div>
    <div class="brand-name">Brightfork<br>Brine Co</div>
    <div class="product-photo" role="img" aria-label="Photo of red strawberry-flavored pickles, one cut open"></div>
    <h2 class="product-title">CRUNCHY PICKLES</h2>
    <div class="flavor-band"><span>STRAWBERRY</span></div>
    <p class="fresh-note">Fresh Packaging</p>
    <div class="care-label">
      <p class="care-title">Liquid Inside</p>
      <p class="care-line">Be careful while opening</p>
      <div class="care-rule"></div>
      <p class="care-line">Refrigerator after opening</p>
    </div>
    <div class="social">
      <p class="follow">Follow Us</p>
      <p class="networks">on our social networks</p>
      <p class="handle">@brightforkbrineco</p>
    </div>
  </section>

</main>
</body>
</html>
```